Design Labels and Brand Look For Mens Soap Company

We are developing a mens soap line for a natural body wash and exfoliating bar. We will be selling this with our line of mens toiletry bags that we sell under the name of Kestrow Totes on Vendora. We are looking for you to design the product brand look with brand color palette and fonts.

The title for the mens body was is "Body Wash For Men". The title for the soap bar is "Exfoliating Bar Soap For Men"

We are providing the templates for these 2 items in PDF form. The final version of the design needs to be in a layered PSD format. You also need to send us the fonts used.

This soap will be sold on Vendora. Do a search for "men's body wash" and "mens soap bar" you will see our competition on page one. We need to stand out with colors and design differentiaon.

Target Market(s)

Men

Industry/Entity Type

Skin Care Product

Requirements
Must have
• Layered PSD file with all fonts

```html
<!DOCTYPE html>
<html lang="en">
<head>
<meta charset="utf-8">
<title>Kestrow Men's Soap Line – Labels and Palette</title>
<link rel="stylesheet" href="https://fonts.googleapis.com/css2?family=Oswald:wght@400;500;600&family=Montserrat:wght@300;400;700;800&family=Playball&family=Open+Sans:wght@700&display=swap">
<style>
  :root {
    --ink: #000000;
    --gold: #d4b47a;
    --maroon: #5a0018;
    --paper: #ffffff;
    --stage: #dddddd;
  }
  * { margin: 0; padding: 0; box-sizing: border-box; }
  html, body { width: 1200px; height: 770px; overflow: hidden; background: var(--stage); }
  .canvas { position: relative; width: 1200px; height: 770px; }
  .rot-up { transform: translate(-50%, -50%) rotate(-90deg); white-space: nowrap; }
  .rot-down { transform: translate(-50%, -50%) rotate(90deg); white-space: nowrap; }

  /* palette */
  .swatch { position: absolute; left: 1079px; width: 105px; height: 31px; }
  .swatch--ink { top: 18px; background: var(--ink); }
  .swatch--gold { top: 53px; background: var(--gold); }
  .swatch--maroon { top: 88px; background: var(--maroon); }
  .swatch--paper { top: 122px; background: var(--paper); }

  /* shared type */
  .brand-name { font-family: "Oswald", sans-serif; font-weight: 500; color: var(--paper); letter-spacing: 1px; line-height: 1; white-space: nowrap; }
  .title { display: inline-block; font-family: "Oswald", sans-serif; font-weight: 600; color: var(--gold); line-height: 1; white-space: nowrap; transform-origin: left top; }
  .for-men { font-family: "Montserrat", sans-serif; font-weight: 800; color: var(--paper); line-height: 1; white-space: nowrap; }
  .blurb { font-family: "Montserrat", sans-serif; font-weight: 300; color: var(--gold); line-height: 1.4; }
  .flag { position: absolute; background: linear-gradient(#b22234 0 50%, #ffffff 50% 60%, #b22234 60%); }
  .flag::before { content: ""; position: absolute; left: 0; top: 0; width: 45%; height: 55%; background: #3c3b6e; }

  /* body wash label */
  .wash-label { position: absolute; left: 45px; top: 449px; width: 525px; height: 281px; background: var(--ink); overflow: hidden; }
  .wash-label .brand-name { position: absolute; left: 262px; top: 49px; font-size: 17px; transform: translate(-50%, -50%); }
  .wash-label .t-moist { position: absolute; left: 204px; top: 83px; font-size: 28px; transform: scaleX(0.755); }
  .wash-label .t-body { position: absolute; left: 204px; top: 102px; font-size: 63px; transform: scaleX(0.87); }
  .wash-label .t-wash { position: absolute; left: 204px; top: 159px; font-size: 57px; transform: scaleX(0.89); }
  .wash-label .for-men { position: absolute; left: 206px; top: 216px; font-size: 21px; letter-spacing: 2.4px; }
  .wash-label .volume { position: absolute; left: 217px; top: 249px; width: 90px; text-align: center; font-family: "Oswald", sans-serif; font-size: 11px; color: var(--gold); }
  .wash-label .tagline { position: absolute; left: 167px; top: 162px; width: 150px; }
  .tagline .script { font-family: "Playball", cursive; color: var(--gold); font-size: 24px; line-height: 1; }
  .tagline .script small { font-family: "Montserrat", sans-serif; font-size: 8px; font-weight: 400; }
  .tagline .uses { font-family: "Montserrat", sans-serif; font-weight: 700; color: var(--paper); font-size: 10.5px; letter-spacing: 2px; line-height: 1; margin-top: -2px; }
  .wash-label .description { position: absolute; left: 357px; top: 161px; width: 148px; font-size: 6.6px; white-space: normal; }
  .wash-label .directions { position: absolute; left: 460px; top: 140px; width: 232px; font-family: "Oswald", sans-serif; font-weight: 400; font-size: 8.4px; line-height: 1.25; color: var(--gold); white-space: normal; }
  .wash-label .contents { position: absolute; left: 495px; top: 140px; width: 232px; font-family: "Oswald", sans-serif; font-weight: 400; font-size: 6.4px; line-height: 1.25; color: var(--gold); white-space: normal; }
  .wash-label .maker { position: absolute; left: 54px; top: 141px; width: 140px; font-family: "Oswald", sans-serif; font-size: 7.2px; line-height: 1.3; color: var(--gold); text-align: center; }
  .wash-label .origin { position: absolute; left: 20px; top: 141px; width: 40px; font-family: "Oswald", sans-serif; font-size: 3.6px; color: var(--paper); text-align: center; }
  .wash-label .flag { left: 26px; top: 127px; width: 13px; height: 26px; }

  /* bar soap wrap */
  .soap-wrap { position: absolute; left: 653px; top: 323px; width: 336px; height: 420px; background: var(--ink); overflow: hidden; }
  .band { position: absolute; background: var(--maroon); color: var(--paper); font-family: "Open Sans", sans-serif; font-weight: 700; display: flex; align-items: center; justify-content: center; white-space: nowrap; }
  .soap-wrap .place { position: absolute; line-height: 1; }
  .soap-wrap .centered { transform: translate(-50%, -50%); }
  .soap-wrap .upside { transform: rotate(180deg); }
  .soap-wrap .upside-centered { transform: translate(-50%, -50%) rotate(180deg); }
  .soap-wrap .description { position: absolute; font-size: 3.4px; line-height: 1.45; font-weight: 400; }
  .soap-wrap .description b { font-weight: 700; }

  /* front panel */
  .soap-front .band { left: 89px; top: 149px; width: 19px; height: 112px; }
  .soap-front .band span { transform: rotate(-90deg); font-size: 8.6px; letter-spacing: 0.6px; }
  .soap-front .t-exf, .soap-front .t-bar { font-size: 29px; transform: scaleX(0.68); }
  .soap-front .for-men { font-size: 8px; letter-spacing: 0.6px; }

  /* lower side panel */
  .soap-side-low .t-exf, .soap-side-low .t-bar { font-size: 24px; transform: scaleX(0.68); }
  .soap-side-low .for-men { font-size: 6.5px; letter-spacing: 0.5px; }

  /* upper, upside-down panels */
  .soap-top .band { left: 76px; top: 34px; width: 184px; height: 15px; }
  .soap-top .band span { display: block; transform: rotate(180deg); font-family: "Oswald", sans-serif; font-weight: 500; font-size: 7.5px; letter-spacing: 0.4px; }
  .soap-top .t-line { font-size: 21px; transform: scaleX(0.62); }
  .soap-top .t-exf { font-size: 25px; transform: scaleX(0.66); }
  .soap-top .t-bar { font-size: 24px; transform: scaleX(0.66); }
  .soap-top .for-men { font-size: 6.5px; letter-spacing: 0.4px; }

  .soap-back { position: absolute; left: 166px; top: 334px; width: 88px; height: 46px; transform: rotate(180deg); }
  .soap-back .fine { font-family: "Montserrat", sans-serif; font-size: 2.7px; line-height: 1.35; color: var(--gold); }
  .soap-back .flag { left: 0; top: 34px; width: 12px; height: 7px; }
  .soap-back .made { position: absolute; left: 0; top: 42px; font-family: "Oswald", sans-serif; font-size: 3px; color: var(--paper); }
</style>
</head>
<body>
<main class="canvas">

  <section class="palette" aria-label="Brand colour palette">
    <div class="swatch swatch--ink"></div>
    <div class="swatch swatch--gold"></div>
    <div class="swatch swatch--maroon"></div>
    <div class="swatch swatch--paper"></div>
  </section>

  <section class="wash-label" aria-label="Moisturizing Body Wash label">
    <div class="flag" role="img" aria-label="United States flag"></div>
    <div class="origin rot-down">MADE IN USA</div>
    <div class="maker rot-down">KESTROW TOTES<br>Larkspur Falls, MN &nbsp;|&nbsp; www.KestrowTotes.com</div>

    <div class="tagline rot-up">
      <div class="script">Premium Wash <small>FOR</small></div>
      <div class="uses">HAIR - FACE - BODY</div>
    </div>

    <div class="brand-name">KESTROW</div>
    <div class="title t-moist">MOISTURIZING</div>
    <div class="title t-body">BODY</div>
    <div class="title t-wash">WASH</div>
    <div class="for-men">For Men</div>
    <div class="volume">16 FL OZ (473 ML)</div>

    <p class="blurb description rot-up">Enriched With Shea Butter, Cocoa Butter, Grapeseed Oil, and Jojoba Oil to moisturize, revitalize and deep clean your skin.</p>
    <p class="directions rot-up">Pour a small amount of our luxurious hand soap into palm of your hand and rub together under water for a rich cleansing lather.</p>
    <p class="contents rot-up">Contains: Water, Sodium Laureth Sulfate, Vegetable Glycerine, ADDITIVES, Sodium Chloride, Fragrance, Citric Acid, Sodium Benzoate, Potassium Sorbate, Vitamin E, Cocoa Butter, Shea Butter, Virgin Olive Oil, Grapeseed Oil, COLOURS.</p>
  </section>

  <section class="soap-wrap" aria-label="Exfoliating Bar Soap wrap">

    <div class="soap-top">
      <p class="blurb description upside" style="left:97px;top:18px;width:148px"><b>Triple Milled Soap</b> Enriched with Shea Butter and Cocoa Butter, Blended With Wheat Bran &amp; Apricot Seed to exfoliate, revitalize, and deep clean your skin.</p>
      <div class="band"><span>Revitalize Your Skin</span></div>

      <div class="side-a">
        <div class="place upside" style="right:126px;top:53px"><span class="for-men">For Men</span></div>
        <div class="place upside" style="right:126px;top:57px"><span class="title t-line">EXFOLIATING BAR SOAP</span></div>
        <div class="place brand-name upside-centered" style="left:230px;top:66px;font-size:7px">KESTROW</div>
      </div>

      <div class="side-b">
        <div class="place upside" style="right:153px;top:90px"><span class="for-men">For Men</span></div>
        <div class="place upside" style="right:153px;top:96px"><span class="title t-bar">BAR SOAP</span></div>
        <div class="place upside" style="right:153px;top:113px"><span class="title t-exf">EXFOLIATING</span></div>
        <div class="place brand-name upside-centered" style="left:214px;top:115px;font-size:10px">KESTROW</div>
      </div>
    </div>

    <div class="soap-front">
      <div class="band"><span>Revitalize Your Skin</span></div>
      <div class="place brand-name centered" style="left:169px;top:170px;font-size:11px">KESTROW</div>
      <div class="place" style="left:121px;top:184px"><span class="title t-exf">EXFOLIATING</span></div>
      <div class="place" style="left:121px;top:206px"><span class="title t-bar">BAR SOAP</span></div>
      <div class="place" style="left:121px;top:230px"><span class="for-men">For Men</span></div>
      <p class="blurb description" style="left:121px;top:243px;width:132px"><b>Triple Milled Soap</b> Enriched with Shea Butter and Cocoa Butter, Blended With Wheat Bran &amp; Apricot Seed to exfoliate, revitalize, and deep clean your skin.</p>
    </div>

    <div class="soap-side-low">
      <div class="place brand-name centered" style="left:120px;top:293px;font-size:9px">KESTROW</div>
      <div class="place" style="left:153px;top:271px"><span class="title t-exf">EXFOLIATING</span></div>
      <div class="place" style="left:153px;top:288px"><span class="title t-bar">BAR SOAP</span></div>
      <div class="place" style="left:153px;top:308px"><span class="for-men">For Men</span></div>
    </div>

    <div class="soap-back">
      <p class="fine">INGREDIENTS:<br>Exfoliating vegetable soap enriched with shea butter &amp; cocoa butter<br>blended wheat bran &amp; apricot seed.</p>
      <p class="fine" style="margin-top:3px">KESTROW TOTES<br>Larkspur Falls, MN<br>www.KestrowTotes.com</p>
      <div class="flag" role="img" aria-label="United States flag"></div>
      <div class="made">MADE IN USA</div>
    </div>
  </section>

</main>
</body>
</html>
```